Redesign Craft Brewing Recipe Website

Originally built with Bootstrap just to get the site going, I am seeking a complete redesign of the sites home page and recipe page. I am an experienced web developer with no graphic background, initially just looking for psd mocks.

I prefer styles that are clean and modern, and would prefer anything that is fun, engaging, and has an organic feel to it. I currently have a cartoon rabbit as a logo, but it needs some modification/tweaking, so any help in that area would be great as well.

Current site:
http://kettlefinch.hostgridapps.net/

Current launch page/logo:
http://www.kettlefinch.com/

I like the overall layout of the elements currently, but the design sucks.
Updates

The launch page is at the following URL

Reason: Still looking for a more modern design. Designs received so far are too similar to the original.

My site is content based and does not contain images or products. Your design should not consist of large images.

Reason: The website has very little images, so the designs need to be more text and content based. The header needs to be very small and should not contain an ad rotater.

Target Market(s)

Home brewers, Craft brewers, Microbreweries, Brewpubs

Requirements
Must have
• Web 2.0 Look and Feel, Fun, Hip, Focus on content
Should not have
• A large photo as a header

```html
<!DOCTYPE html>
<html lang="en">
<head>
<meta charset="utf-8">
<title>Kettlefinch – Latest Recipes</title>
<link rel="stylesheet" href="https://fonts.googleapis.com/css2?family=Roboto:wght@300;400;500;700&family=Roboto+Condensed:wght@400;700&display=swap">
<style>
  :root{
    --bg-green:#2f5b46;
    --bg-green-dark:#264c3a;
    --header-dark:#050b09;
    --header-glow:#123a32;
    --brand-green:#2fa85a;
    --panel:#fbfbfb;
    --ink:#333;
    --muted:#8a8a8a;
    --blue:#35a8d6;
    --red:#de4a4a;
    --line:#e4e4e4;
    --field-border:#dedede;
    --footer-bar:#0c0c0c;
  }
  *{box-sizing:border-box;margin:0;padding:0}
  html,body{width:1014px;height:1200px;overflow:hidden}
  body{
    position:relative;
    background:radial-gradient(circle at 50% 40%,var(--bg-green),var(--bg-green-dark));
    font-family:"Roboto",sans-serif;color:var(--ink);
  }
  .site-header{
    position:absolute;left:0;top:0;width:1014px;height:136px;
    background:radial-gradient(ellipse 320px 140px at 50% 40%,var(--header-glow),var(--header-dark));
    text-align:center;
  }
  .brand{
    position:absolute;left:0;right:0;top:68px;
    font-family:"Roboto",sans-serif;font-weight:500;font-size:36px;line-height:1;
    color:var(--brand-green);letter-spacing:.5px;
  }
  .tagline{
    position:absolute;left:0;right:0;top:106px;
    font-size:11.5px;line-height:14px;color:#fff;
  }

  .sidebar{
    position:absolute;left:93px;top:138px;width:201px;height:1014px;
    background:var(--panel);border-radius:0 0 3px 3px;
  }
  .sidebar h2{
    position:absolute;left:16px;
    font-family:"Roboto",sans-serif;font-weight:500;font-size:18px;color:#333;
  }
  .sidebar h2 .accent{color:var(--blue)}
  .field{
    position:absolute;left:11px;width:178px;height:26px;
    border:1px solid var(--field-border);background:#fff;
    font-size:11.5px;color:#555;padding:0 0 0 19px;line-height:24px;
  }
  .field.placeholder{color:#b0b0b0;padding-left:19px}
  .field .caret{
    position:absolute;right:14px;top:11px;width:0;height:0;
    border-left:4px solid transparent;border-right:4px solid transparent;border-top:5px solid #555;
  }
  .field .dot{
    position:absolute;right:18px;top:9px;width:7px;height:7px;border-radius:50%;
    border:1px solid #777;background:radial-gradient(circle,#333 35%,#fff 45%);
  }
  .range-label{position:absolute;left:13px;top:320px;font-size:10.5px;color:#444}
  .slider{position:absolute;left:11px;top:342px;width:178px;height:8px;
    border-radius:4px;background:#e8e8e8;border:1px solid #d3d3d3}
  .slider-fill{position:absolute;left:47px;top:1px;width:112px;height:4px;background:#7ab8e4;border-radius:2px}
  .handle{position:absolute;top:-5px;width:11px;height:14px;border-radius:3px;
    background:linear-gradient(#fff,#ddd);border:1px solid #aaa}
  .ticks{position:absolute;left:11px;top:362px;width:180px;font-size:8px;font-weight:700;color:#444}
  .ticks span{position:absolute}
  .update-btn{
    position:absolute;left:7px;top:427px;width:186px;height:27px;
    background:linear-gradient(#3a3a3a,#111);color:#fff;border-radius:2px;
    font-family:"Roboto Condensed",sans-serif;font-weight:700;font-size:12px;
    text-align:center;line-height:27px;letter-spacing:.3px;
  }

  .content{
    position:absolute;left:302px;top:138px;width:620px;height:1014px;
    background:var(--panel);
  }
  .content h1{
    position:absolute;left:16px;top:16px;
    font-family:"Roboto Condensed",sans-serif;font-weight:700;font-size:37px;line-height:1;color:#3a3a3a;
  }
  .content h1 .accent{color:var(--blue)}
  .tabs{position:absolute;left:19px;top:65px;font-size:13px;color:#222}
  .tabs .active{color:var(--red)}
  .tabs .sep{margin:0 9px}
  .tabs-rule{position:absolute;left:5px;right:0;top:89px;border-top:1px solid var(--line)}

  .recipe-row{position:absolute;left:5px;width:620px;height:219px;border-bottom:1px solid var(--line)}
  .recipe-row:last-of-type{border-bottom:none}
  .recipe{position:absolute;top:0;width:300px;height:170px}
  .recipe:nth-child(1){left:7px}
  .recipe:nth-child(2){left:317px}
  .recipe-photo{
    position:absolute;left:0;top:14px;width:79px;height:83px;border:1px solid #e2e2e2;
    background:linear-gradient(90deg,#fff 0,#fff 10%,#6b7a2a 14%,#2a2a2a 22%,#fff 26%,#fff 38%,#b52a32 42%,#3a1a1a 50%,#fff 54%,#fff 66%,#2a1a22 70%,#111 78%,#fff 82%);
  }
  .tag{
    position:absolute;left:0;width:79px;height:26px;color:#fff;
    font-family:"Roboto Condensed",sans-serif;font-size:13.5px;text-align:center;line-height:26px;
  }
  .tag.method{top:103px;background:var(--red)}
  .tag.style{top:134px;background:var(--blue)}
  .recipe h3{
    position:absolute;left:87px;top:18px;width:150px;
    font-family:"Roboto Condensed",sans-serif;font-weight:400;font-size:16px;line-height:15.5px;color:#333;
  }
  .byline{position:absolute;left:87px;top:53px;font-family:"Roboto Condensed",sans-serif;font-size:10.5px;color:#aaa}
  .byline b{font-weight:400;color:#333}
  .summary{position:absolute;left:87px;top:72px;width:160px;font-size:10.5px;line-height:15.2px;color:#8c8c8c;font-weight:300}
  .stats{
    position:absolute;left:250px;top:0;width:40px;height:168px;background:var(--blue);
    color:#fff;font-size:8px;font-weight:700;text-align:center;line-height:9.5px;
  }
  .stats .stat{position:absolute;left:0;width:40px}
  .stats .srm{position:absolute;left:0;bottom:0;width:40px;height:33px;background:var(--red);padding-top:9px}

  .results-bar{
    position:absolute;left:0;bottom:0;width:620px;height:45px;background:var(--footer-bar);color:#fff;
    font-family:"Roboto Condensed",sans-serif;font-weight:700;font-size:12.5px;
  }
  .results-bar .label{position:absolute;left:92px;top:15px}
  .results-bar .count{position:absolute;left:199px;top:15px}
  .pager{position:absolute;top:13px;width:41px;height:20px;background:#fff;color:#333;
    border-radius:2px;font-size:10.5px;text-align:center;line-height:20px}
  .pager.prev{left:500px}
  .pager.next{left:551px}
  .copyright{position:absolute;right:97px;top:1172px;font-size:9px;color:rgba(255,255,255,.12)}
</style>
</head>
<body>
  <header class="site-header">
    <div class="brand">Kettlefinch</div>
    <p class="tagline">Easiest way to create and share<br>craft beer recipes.</p>
  </header>

  <aside class="sidebar">
    <h2 style="top:29px">Search <span class="accent">Recipes</span></h2>
    <div class="field placeholder" style="top:56px">Stout</div>
    <h2 style="top:105px">Match Maker</h2>
    <div class="field" style="top:130px;font-size:12.5px">Boil Size<span class="dot"></span></div>
    <h2 style="top:181px">Brewing</h2>
    <div class="field" style="top:205px">Extract<span class="caret"></span></div>
    <h2 style="top:256px">Styles</h2>
    <div class="field" style="top:279px">American Amber Ale<span class="caret"></span></div>
    <div class="range-label">0 Gals to 25 Gals</div>
    <div class="slider">
      <div class="slider-fill"></div>
      <div class="handle" style="left:41px"></div>
      <div class="handle" style="left:153px"></div>
    </div>
    <div class="ticks">
      <span style="left:0">0</span><span style="left:30px">5</span><span style="left:64px">10</span>
      <span style="left:99px">15</span><span style="left:134px">20</span><span style="left:164px">25</span>
    </div>
    <div class="update-btn">UPDATE SEARCH</div>
  </aside>

  <main class="content">
    <h1>Latest <span class="accent">Recipes</span></h1>
    <nav class="tabs"><span class="active">Popular</span><span class="sep">/</span>Recent</nav>
    <div class="tabs-rule"></div>

    <section class="recipe-row" style="top:99px">
      <article class="recipe">
        <div class="recipe-photo" role="img" aria-label="Three wine bottles: green, red and dark"></div>
        <div class="tag method">Extract</div><div class="tag style">Sweet Mead</div>
        <h3>Oak Hollow Sweet Mead</h3>
        <p class="byline">Created by <b>Dana Whitlow</b></p>
        <p class="summary">Le Lorem Ipsum est simplement du faux texte employé dans la composition mise en page avant impression. Lorem Ipsum est le faux texte merie depuis les années 1500.</p>
        <div class="stats"><div class="stat" style="top:11px">2.24%<br>abv</div><div class="stat" style="top:46px">24<br>ibu</div><div class="stat" style="top:79px">1.006<br>fb</div><div class="stat" style="top:113px">1.022<br>og</div><div class="srm">9<br>SRM</div></div>
      </article>
      <article class="recipe">
        <div class="recipe-photo" role="img" aria-label="Three wine bottles: green, red and dark"></div>
        <div class="tag method">Extract</div><div class="tag style">Sweet Mead</div>
        <h3>Oak Hollow Sweet Mead</h3>
        <p class="byline">Created by <b>Dana Whitlow</b></p>
        <p class="summary">Le Lorem Ipsum est simplement du faux texte employé dans la composition mise en page avant impression. Lorem Ipsum est le faux texte merie depuis les années 1500.</p>
        <div class="stats"><div class="stat" style="top:11px">2.24%<br>abv</div><div class="stat" style="top:46px">24<br>ibu</div><div class="stat" style="top:79px">1.006<br>fb</div><div class="stat" style="top:113px">1.022<br>og</div><div class="srm">9<br>SRM</div></div>
      </article>
    </section>

    <section class="recipe-row" style="top:318px">
      <article class="recipe">
        <div class="recipe-photo" role="img" aria-label="Three wine bottles: green, red and dark"></div>
        <div class="tag method">Extract</div><div class="tag style">Sweet Mead</div>
        <h3>Oak Hollow Sweet Mead</h3>
        <p class="byline">Created by <b>Dana Whitlow</b></p>
        <p class="summary">Le Lorem Ipsum est simplement du faux texte employé dans la composition mise en page avant impression. Lorem Ipsum est le faux texte merie depuis les années 1500.</p>
        <div class="stats"><div class="stat" style="top:11px">2.24%<br>abv</div><div class="stat" style="top:46px">24<br>ibu</div><div class="stat" style="top:79px">1.006<br>fb</div><div class="stat" style="top:113px">1.022<br>og</div><div class="srm">9<br>SRM</div></div>
      </article>
      <article class="recipe">
        <div class="recipe-photo" role="img" aria-label="Three wine bottles: green, red and dark"></div>
        <div class="tag method">Extract</div><div class="tag style">Sweet Mead</div>
        <h3>Oak Hollow Sweet Mead</h3>
        <p class="byline">Created by <b>Dana Whitlow</b></p>
        <p class="summary">Le Lorem Ipsum est simplement du faux texte employé dans la composition mise en page avant impression. Lorem Ipsum est le faux texte merie depuis les années 1500.</p>
        <div class="stats"><div class="stat" style="top:11px">2.24%<br>abv</div><div class="stat" style="top:46px">24<br>ibu</div><div class="stat" style="top:79px">1.006<br>fb</div><div class="stat" style="top:113px">1.022<br>og</div><div class="srm">9<br>SRM</div></div>
      </article>
    </section>

    <section class="recipe-row" style="top:537px">
      <article class="recipe">
        <div class="recipe-photo" role="img" aria-label="Three wine bottles: green, red and dark"></div>
        <div class="tag method">Extract</div><div class="tag style">Sweet Mead</div>
        <h3>Oak Hollow Sweet Mead</h3>
        <p class="byline">Created by <b>Dana Whitlow</b></p>
        <p class="summary">Le Lorem Ipsum est simplement du faux texte employé dans la composition mise en page avant impression. Lorem Ipsum est le faux texte merie depuis les années 1500.</p>
        <div class="stats"><div class="stat" style="top:11px">2.24%<br>abv</div><div class="stat" style="top:46px">24<br>ibu</div><div class="stat" style="top:79px">1.006<br>fb</div><div class="stat" style="top:113px">1.022<br>og</div><div class="srm">9<br>SRM</div></div>
      </article>
      <article class="recipe">
        <div class="recipe-photo" role="img" aria-label="Three wine bottles: green, red and dark"></div>
        <div class="tag method">Extract</div><div class="tag style">Sweet Mead</div>
        <h3>Oak Hollow Sweet Mead</h3>
        <p class="byline">Created by <b>Dana Whitlow</b></p>
        <p class="summary">Le Lorem Ipsum est simplement du faux texte employé dans la composition mise en page avant impression. Lorem Ipsum est le faux texte merie depuis les années 1500.</p>
        <div class="stats"><div class="stat" style="top:11px">2.24%<br>abv</div><div class="stat" style="top:46px">24<br>ibu</div><div class="stat" style="top:79px">1.006<br>fb</div><div class="stat" style="top:113px">1.022<br>og</div><div class="srm">9<br>SRM</div></div>
      </article>
    </section>

    <section class="recipe-row" style="top:759px;border-bottom:none">
      <article class="recipe">
        <div class="recipe-photo" role="img" aria-label="Three wine bottles: green, red and dark"></div>
        <div class="tag method">Extract</div><div class="tag style">Sweet Mead</div>
        <h3>Oak Hollow Sweet Mead</h3>
        <p class="byline">Created by <b>Dana Whitlow</b></p>
        <p class="summary">Le Lorem Ipsum est simplement du faux texte employé dans la composition mise en page avant impression. Lorem Ipsum est le faux texte merie depuis les années 1500.</p>
        <div class="stats"><div class="stat" style="top:11px">2.24%<br>abv</div><div class="stat" style="top:46px">24<br>ibu</div><div class="stat" style="top:79px">1.006<br>fb</div><div class="stat" style="top:113px">1.022<br>og</div><div class="srm">9<br>SRM</div></div>
      </article>
      <article class="recipe">
        <div class="recipe-photo" role="img" aria-label="Three wine bottles: green, red and dark"></div>
        <div class="tag method">Extract</div><div class="tag style">Sweet Mead</div>
        <h3>Oak Hollow Sweet Mead</h3>
        <p class="byline">Created by <b>Dana Whitlow</b></p>
        <p class="summary">Le Lorem Ipsum est simplement du faux texte employé dans la composition mise en page avant impression. Lorem Ipsum est le faux texte merie depuis les années 1500.</p>
        <div class="stats"><div class="stat" style="top:11px">2.24%<br>abv</div><div class="stat" style="top:46px">24<br>ibu</div><div class="stat" style="top:79px">1.006<br>fb</div><div class="stat" style="top:113px">1.022<br>og</div><div class="srm">9<br>SRM</div></div>
      </article>
    </section>

    <footer class="results-bar">
      <span class="label">Search Result</span>
      <span class="count">12 Found</span>
      <span class="pager prev">Prev</span>
      <span class="pager next">Next</span>
    </footer>
  </main>

  <p class="copyright">Copyright © 2013 Kettlefinch. All rights reserved.</p>
</body>
</html>
```